Live Webcasting Host Wants Template/Theme to Jumpstare Ecommerce Site

Please,Please, Please READ ALL OF THE DESCRIPTION. Thank you.

I need a template for a look for my developer to work with in designing an ecommerce site where clients pay a monthly fee for streaming services and video on demand.

I'll need 2 pages designed:
1) public page
2) client log in landing page.

Please use a CMS (WP preferred) as this will allow is for further content to be added after delivery. Please include the pricing text in boxes in slides (pdf) to help fill out you design for the home page.

The attached slides are to give you a general layout of how I envision the pages. Yes I would like the Client page to be tabbed from the side like in the attached slide.

I've attached company logos for use along with the accompanying .psd and .ai files in the zip. Use the colors in logo in site design.

Thank you for your time.
Updates

Please, no designs. This is for a CMS for webpage design like WordPress or Joomla. Thanks. Added Friday, January 13, 2017

Reason: Looking for more designs.

Target Market(s)

Churches, Organizations, Civic Organizations, Government Agencies (State, Local) -BUT don't let this deter your creativity. Decision makers/influencers will be video production and/or IT personnel.

Industry/Entity Type

It Company

Font styles to use
Sans Serif

Colors
f5f5f5
e8e8e8
333333
fece3e
cbcbcb
33a6d7
000000

Requirements
Must have
• Responsive Design
Nice to have
• One Page Design
Should not have
• SHOULD NOT HAVE White overall background but use white in other ways if you like.

```html
<!DOCTYPE html>
<html lang="en">
<head>
<meta charset="utf-8">
<title>Velora — Pricing</title>
<link href="https://fonts.googleapis.com/css2?family=Noto+Sans:wght@400;700&display=swap" rel="stylesheet">
<style>
:root{
  --orange:#f79c22;
  --orange-dark:#d57f12;
  --blue:#33a6d7;
  --charcoal:#333333;
  --yellow:#fece3e;
  --band-top:#fdcb3f;
  --band-bottom:#efe4c6;
  --white:#ffffff;
  --text:#333333;
  --muted:#555555;
  --footer-text:#444444;
  --social:#a3a3a3;
}
*{box-sizing:border-box;margin:0;padding:0}
html,body{width:1200px;height:695px;overflow:hidden}
body{font-family:"Noto Sans",Arial,sans-serif;color:var(--text);background:var(--white);position:relative}

.site-header{position:absolute;left:0;top:0;width:1200px;height:96px;background:var(--white)}
.brand{position:absolute;left:74px;top:22px;font-size:40px;font-weight:700;color:var(--charcoal);line-height:48px;letter-spacing:-1px;text-decoration:none}
.main-nav{position:absolute;left:368px;top:38px;display:flex;gap:31px}
.main-nav a{font-size:15px;font-weight:700;color:var(--charcoal);text-decoration:none;letter-spacing:.2px}
.login-btn{position:absolute;left:1040px;top:29px;width:84px;height:35px;background:var(--orange);color:var(--white);font-size:14px;font-weight:700;display:flex;align-items:center;justify-content:center;border-radius:2px;text-decoration:none}

.pricing{position:absolute;left:0;top:96px;width:1200px;height:544px;background:linear-gradient(to bottom,var(--band-top),var(--band-bottom))}
.plan{position:absolute;top:66px;width:331px;height:413px;background:var(--white);box-shadow:0 14px 14px -8px rgba(0,0,0,.28)}
.plan-small{left:73px}
.plan-medium{left:434px}
.plan-large{left:793px}
.plan-head{height:101px;text-align:center;color:var(--white);font-size:20px;font-weight:700;padding-top:18px}
.plan-small .plan-head{background:var(--orange)}
.plan-medium .plan-head{background:var(--blue)}
.plan-large .plan-head{background:var(--charcoal)}
.plan-price{position:absolute;left:124px;top:61px;width:83px;height:83px;border-radius:50%;background:var(--yellow);border:3px solid var(--white);display:flex;align-items:center;justify-content:center;font-size:22px;font-weight:700;color:var(--charcoal)}
.plan-icon{position:absolute;left:28px;top:164px}
.plan-body{position:absolute;left:92px;top:164px;width:215px}
.plan-hours{font-size:28px;font-weight:700;line-height:28px}
.plan-unit{font-size:17px;font-weight:700;line-height:20px}
.plan-note{font-size:15px;color:var(--muted);line-height:19px;margin-top:4px}
.plan-storage{font-size:15px;font-weight:700;color:var(--muted);line-height:19px;margin-top:22px;width:180px}
.buy-btn{position:absolute;left:93px;top:343px;width:165px;height:48px;background:var(--orange);border-radius:4px;box-shadow:0 3px 0 var(--orange-dark);display:flex;color:var(--white);text-decoration:none;overflow:hidden}
.buy-label{flex:1;display:flex;align-items:center;justify-content:center;font-size:16px;font-weight:700}
.buy-arrow{width:38px;background:var(--orange-dark);opacity:.85;display:flex;align-items:center;justify-content:center}

.site-footer{position:absolute;left:0;top:640px;width:1200px;height:55px;background:var(--white)}
.legal{position:absolute;left:79px;top:16px;font-size:14px;color:var(--footer-text)}
.legal span{margin:0 8px}
.social{position:absolute;right:76px;top:13px;display:flex;gap:2px}
.social i{width:25px;height:25px;background:var(--social);display:block}
</style>
</head>
<body>
<header class="site-header">
  <a class="brand" href="#">Velora</a>
  <nav class="main-nav">
    <a href="#">FEATURES</a><a href="#">PRICING</a><a href="#">ABOUT US</a><a href="#">WEBCASTING 101</a><a href="#">CONTACT</a>
  </nav>
  <a class="login-btn" href="#">LOG IN</a>
</header>

<main class="pricing">
  <section class="plan plan-small">
    <div class="plan-head">SMALL</div>
    <div class="plan-price">$49</div>
    <svg class="plan-icon" width="46" height="48" viewBox="0 0 46 48" fill="none" stroke="#333" stroke-width="2.4"><path d="M24 8H2v28h42V20"/><path d="M14 18l12 7-12 7z" fill="#333" stroke="none"/><path d="M2 42h34M40 42h2"/><circle cx="35" cy="10" r="8" fill="#fff"/><path d="M35 6v4h3"/></svg>
    <div class="plan-body">
      <div class="plan-hours">400</div>
      <div class="plan-unit">Viewer Hours</div>
      <div class="plan-note">(50 Viewers watching 2 hrs- 4 times per month)</div>
      <div class="plan-storage">100 GB/month of video Storage</div>
    </div>
    <a class="buy-btn" href="#"><span class="buy-label">Buy Package</span><span class="buy-arrow"><svg width="20" height="14" viewBox="0 0 20 14"><path d="M12 0l8 6-8 6V8C6 8 3 10 0 14 1 8 5 4 12 4z" fill="#fff"/></svg></span></a>
  </section>

  <section class="plan plan-medium">
    <div class="plan-head">MEDIUM</div>
    <div class="plan-price">$399</div>
    <svg class="plan-icon" width="46" height="48" viewBox="0 0 46 48" fill="none" stroke="#333" stroke-width="2.4"><path d="M24 8H2v28h42V20"/><path d="M14 18l12 7-12 7z" fill="#333" stroke="none"/><path d="M2 42h34M40 42h2"/><circle cx="35" cy="10" r="8" fill="#fff"/><path d="M35 6v4h3"/></svg>
    <div class="plan-body">
      <div class="plan-hours">4000</div>
      <div class="plan-unit">Viewer Hours</div>
      <div class="plan-note">(500 Viewers watching 2 hrs- 4 times per month)</div>
      <div class="plan-storage">500 GB/month of video Storage</div>
    </div>
    <a class="buy-btn" href="#"><span class="buy-label">Buy Package</span><span class="buy-arrow"><svg width="20" height="14" viewBox="0 0 20 14"><path d="M12 0l8 6-8 6V8C6 8 3 10 0 14 1 8 5 4 12 4z" fill="#fff"/></svg></span></a>
  </section>

  <section class="plan plan-large">
    <div class="plan-head">LARGE</div>
    <div class="plan-price">$999</div>
    <svg class="plan-icon" width="46" height="48" viewBox="0 0 46 48" fill="none" stroke="#333" stroke-width="2.4"><path d="M24 8H2v28h42V20"/><path d="M14 18l12 7-12 7z" fill="#333" stroke="none"/><path d="M2 42h34M40 42h2"/><circle cx="35" cy="10" r="8" fill="#fff"/><path d="M35 6v4h3"/></svg>
    <div class="plan-body">
      <div class="plan-hours">16000</div>
      <div class="plan-unit">Viewer Hours</div>
      <div class="plan-note">(2000 Viewers watching 2 hrs- 4 times per month)</div>
      <div class="plan-storage">2000 GB/month of video Storage</div>
    </div>
    <a class="buy-btn" href="#"><span class="buy-label">Buy Package</span><span class="buy-arrow"><svg width="20" height="14" viewBox="0 0 20 14"><path d="M12 0l8 6-8 6V8C6 8 3 10 0 14 1 8 5 4 12 4z" fill="#fff"/></svg></span></a>
  </section>
</main>

<footer class="site-footer">
  <div class="legal">© 2017 Velora. All rights reserved<span>|</span>Privacy Policy<span>|</span>Terms of Use</div>
  <div class="social"><i></i><i></i><i></i></div>
</footer>
</body>
</html>
```